Business card design needed for Automotive Reconditioning business

I have a logo design i just cant decide on the best color or layout for the business card, I will upload all the files so you can see all colors schemes we are considering. I have other file formats if needed let me know.

Target Market(s)

automotive dealerships

Contact Information for Business Card

HERE are the Descriptions and info needed on the card:
Interior Repair: Leather carpet burns panels dash Deoderize
Dealer products and Vin Verify
( spot for name and cell number) My name is Norman Bexley phone 614 352-4180 Title COO www.QuorvalMotive.com

Font styles to use
Sans Serif
Other font styles liked:
• what ever you think looks best

Requirements
Must have
• Must be able to change the name and phone for employees

```html
<!DOCTYPE html>
<html lang="en">
<head>
<meta charset="utf-8">
<title>Quorval Motive – Business Card</title>
<link href="https://fonts.googleapis.com/css2?family=Raleway:wght@500;600;700&display=swap" rel="stylesheet">
<style>
  :root {
    --page: #e9e5df;
    --card-deep: #0d1540;
    --card-glow: #1d2763;
    --ink: #ffffff;
    --rule: #c9cde0;
    --accent-red: #e8432b;
    --accent-blue: #2a8fd6;
    --pill: #243a86;
  }
  html, body {
    margin: 0;
    width: 1200px;
    height: 1200px;
    overflow: hidden;
    background: var(--page);
    font-family: "Raleway", sans-serif;
    font-variant-numeric: lining-nums;
  }
  .card {
    position: absolute;
    left: 150px;
    top: 330px;
    width: 900px;
    height: 540px;
    border-radius: 32px;
    background: radial-gradient(ellipse at 55% 50%, var(--card-glow) 0%, var(--card-deep) 70%);
    color: var(--ink);
    overflow: hidden;
  }
  .name-bars { position: absolute; left: 82px; top: 108px; display: flex; gap: 7px; }
  .name-bars span { width: 14px; height: 68px; display: block; }
  .name-bars .red { background: var(--accent-red); }
  .name-bars .blue { background: var(--accent-blue); }
  .person-name {
    position: absolute; left: 141px; top: 112px; margin: 0;
    font-size: 30px; font-weight: 600; letter-spacing: 0.2px; text-transform: uppercase;
    white-space: nowrap;
  }
  .person-title {
    position: absolute; left: 150px; top: 156px; margin: 0;
    font-size: 28px; font-weight: 500;
  }
  .brand {
    position: absolute; left: 452px; top: 116px; width: 380px;
    display: flex; align-items: center; gap: 14px;
  }
  .brand-mark { width: 20px; height: 20px; background: var(--accent-red); flex: none; }
  .brand-name {
    margin: 0; font-size: 26px; font-weight: 700; line-height: 1.2; color: var(--ink);
    text-transform: uppercase; white-space: nowrap;
  }
  .divider {
    position: absolute; left: 64px; width: 780px; height: 1px; background: var(--rule);
  }
  .divider.first { top: 226px; }
  .divider.second { top: 236px; }
  .services {
    position: absolute; left: 81px; top: 288px; margin: 0;
    font-size: 26px; font-weight: 500; line-height: 32px;
  }
  .services strong { font-weight: 700; }
  .dealer-pill {
    position: absolute; left: 82px; top: 368px; height: 44px; width: 408px;
    background: var(--pill);
    border-radius: 18px 0 0 18px;
    clip-path: polygon(0 0, 96% 0, 100% 40%, 100% 100%, 0 100%);
    display: flex; align-items: center; padding-left: 14px; box-sizing: border-box;
    font-size: 26px; font-weight: 600;
  }
  .phone {
    position: absolute; left: 577px; top: 422px;
    display: flex; align-items: center; gap: 20px;
    font-size: 29px; font-weight: 600; letter-spacing: 0.5px;
  }
  .phone svg { width: 44px; height: 44px; flex: none; }
</style>
</head>
<body>
  <section class="card">
    <div class="name-bars"><span class="red"></span><span class="blue"></span></div>
    <h1 class="person-name">Norman Bexley</h1>
    <p class="person-title">COO</p>

    <div class="brand">
      <span class="brand-mark"></span>
      <p class="brand-name">Quorval Motive<br>Reconditioning Corp.</p>
    </div>

    <div class="divider first"></div>
    <div class="divider second"></div>

    <p class="services"><strong>Interior Repair:</strong> Leather carpet<br>burns panels dash Deoderize</p>
    <div class="dealer-pill">Dealer products and Vin Verify</div>

    <div class="phone">
      <svg viewBox="0 0 44 44" aria-hidden="true">
        <circle cx="22" cy="22" r="21" fill="var(--accent-red)" stroke="var(--accent-blue)" stroke-width="2"/>
        <path d="M15 12c1-1 2.5-1 3.2.2l2 3.3c.5.9.3 2-.5 2.6l-1.3 1c1 2.6 3 4.7 5.6 5.8l1-1.3c.7-.8 1.8-1 2.6-.4l3.3 2c1.1.7 1.2 2.3.2 3.2l-1.6 1.5c-1.3 1.2-3.2 1.5-4.8.8-5.5-2.4-9.7-6.7-12-12.2-.6-1.6-.3-3.4.9-4.7z" fill="#ffffff"/>
      </svg>
      <span>614 352-4180</span>
    </div>
  </section>
</body>
</html>
```